Bourbon label design for bourbon brand. Looking to freshen our current label.

I need a Bourbon label design for our rebranded Bourbon bottle. Label should include picture of our horse and our logo on the bottle. Front Label is 3.5 inches wide and 6 inches tall, back label is 4 inches tall and 3 inches wide. Back label can be a simple plain logo like the one in the brief. I have included a design of our current bottle and label. We want to stay close to the current color schemes but want a fresh rebrand of the design. The label needs to be the correct size on a tall bottle like pictured.

Target Market(s)

Our Bourbon members, 30-50 year old males

Requirements
Must have
• Picture of our horse, our B logo , straight Bourbon whiskey on the front. Room to edit text on the back label.

```html
<!DOCTYPE html>
<html lang="en">
<head>
<meta charset="utf-8">
<title>Nightfall Straight Bourbon Whiskey – Label Set</title>
<link rel="stylesheet" href="https://fonts.googleapis.com/css2?family=Michroma&family=Space+Grotesk:wght@400;500;700&family=Bebas+Neue&display=swap">
<style>
  :root {
    --page: #ffffff;
    --ink: #ffffff;
    --label-top: #4a4a4a;
    --label-mid: #2a2a2a;
    --label-bottom: #050505;
    --silver-light: #f2f2f2;
    --silver-dark: #8d8d8d;
    --title-silver: #c9c9c9;
    --divider: #e4e4e4;
  }
  * { margin: 0; padding: 0; box-sizing: border-box; }
  html, body { width: 1200px; height: 1036px; overflow: hidden; background: var(--page); }
  .canvas { position: relative; width: 1200px; height: 1036px; background: var(--page); }
  .divider { position: absolute; left: 600px; top: 0; width: 1px; height: 1036px; background: var(--divider); }

  /* Front label */
  .front-label { position: absolute; left: 50px; top: 89px; width: 501px; height: 858px; overflow: hidden; color: var(--ink); }
  .front-photo {
    position: absolute; inset: 0;
    background:
      radial-gradient(ellipse 60% 40% at 45% 25%, rgba(150,150,150,.55), transparent 70%),
      linear-gradient(180deg, var(--label-top) 0%, var(--label-mid) 45%, #121212 70%, var(--label-bottom) 100%);
  }
  .silver-band { position: absolute; left: 0; width: 501px; }
  .silver-band.top { top: 0; }
  .silver-band.bottom { bottom: 0; }
  .brand-title {
    position: absolute; top: 336px; left: 0; width: 100%; text-align: center;
    font-family: "Michroma", sans-serif; font-size: 48px; letter-spacing: 1px; color: var(--title-silver);
  }
  .style-line {
    position: absolute; top: 396px; left: 0; width: 100%; text-align: center;
    font-family: "Michroma", sans-serif; font-size: 14.5px; letter-spacing: .5px;
  }
  .badge-text {
    position: absolute; top: 506px; text-align: center;
    font-family: "Bebas Neue", sans-serif; font-size: 28px; line-height: 31px; letter-spacing: .5px;
  }
  .badge-text.left { left: 60px; width: 80px; }
  .badge-text.right { left: 340px; width: 90px; }
  .brand-mark { position: absolute; top: 464px; left: 170px; width: 160px; height: 140px; text-align: center; }
  .brand-mark .ring { width: 76px; height: 76px; margin: 0 auto 10px; border: 3px solid var(--ink); border-radius: 50%; }
  .brand-mark .name { font-family: "Bebas Neue", sans-serif; font-size: 34px; line-height: 36px; letter-spacing: 1px; }
  .age-mark { position: absolute; top: 687px; left: 176px; width: 148px; height: 70px; }
  .age-mark .rule { position: absolute; left: 0; width: 148px; height: 1.5px; background: var(--silver-dark); }
  .age-mark .word { position: absolute; top: 34px; font-family: "Bebas Neue", sans-serif; font-size: 24px; line-height: 24px; color: #d9d9d9; }
  .age-mark .num { position: absolute; left: 46px; top: 0; width: 56px; text-align: center; font-family: "Bebas Neue", sans-serif; font-size: 70px; line-height: 64px; color: #e8e8e8; }
  .field-label { position: absolute; top: 755px; font-family: "Space Grotesk", sans-serif; font-weight: 500; font-size: 11px; text-align: center; width: 70px; }
  .field-box { position: absolute; top: 773px; width: 57px; height: 57px; background: var(--ink); }

  /* Back label */
  .back-label { position: absolute; left: 685px; top: 232px; width: 429px; height: 571px; overflow: hidden; color: var(--ink); text-align: center; font-family: "Space Grotesk", sans-serif; }
  .back-photo {
    position: absolute; inset: 0;
    background:
      radial-gradient(ellipse 55% 35% at 55% 28%, rgba(140,140,140,.45), transparent 70%),
      linear-gradient(180deg, #3c3c3c 0%, #2a2a2a 40%, #151515 70%, #050505 100%);
  }
  .company-mark { position: absolute; top: 22px; left: 0; width: 100%; }
  .company-mark .ring { width: 46px; height: 46px; margin: 0 auto 10px; border: 2.5px solid var(--ink); border-radius: 50%; }
  .company-mark .name { font-weight: 700; font-size: 17px; line-height: 16px; letter-spacing: .3px; }
  .company-mark .sub { margin-top: 4px; font-weight: 400; font-size: 7px; letter-spacing: 3px; }
  .edition { position: absolute; top: 150px; left: 0; width: 100%; font-weight: 700; font-size: 21px; line-height: 30px; }
  .story { position: absolute; left: 36px; width: 357px; font-weight: 500; font-size: 11.5px; line-height: 15.5px; }
  .story.one { top: 248px; }
  .story.two { top: 322px; }
  .maker { position: absolute; top: 385px; left: 0; width: 100%; font-weight: 700; font-size: 12.5px; line-height: 17px; }
  .site { position: absolute; top: 421px; left: 0; width: 100%; font-weight: 700; font-size: 19px; }
  .warning { position: absolute; top: 451px; left: 27px; width: 378px; text-align: justify; font-weight: 400; font-size: 11px; line-height: 15.5px; }
  .volume { position: absolute; top: 536px; left: 0; width: 100%; font-weight: 700; font-size: 18px; }
</style>
</head>
<body>
<main class="canvas">
  <div class="divider"></div>

  <section class="front-label">
    <div class="front-photo" role="img" aria-label="Black and white photo of the racing horse and jockey charging forward"></div>
    <svg class="silver-band top" width="501" height="20" viewBox="0 0 501 20" aria-hidden="true">
      <defs>
        <linearGradient id="silverSheen" x1="0" x2="1">
          <stop offset="0" stop-color="#8d8d8d"/><stop offset=".3" stop-color="#f2f2f2"/>
          <stop offset=".6" stop-color="#9a9a9a"/><stop offset=".85" stop-color="#f0f0f0"/><stop offset="1" stop-color="#8d8d8d"/>
        </linearGradient>
      </defs>
      <polygon points="0,0 501,0 501,0 0,18" fill="url(#silverSheen)"/>
    </svg>
    <svg class="silver-band bottom" width="501" height="20" viewBox="0 0 501 20" aria-hidden="true">
      <polygon points="0,2 501,20 0,20" fill="url(#silverSheen)"/>
    </svg>

    <h1 class="brand-title">NIGHTFALL</h1>
    <p class="style-line">STRAIGHT BOURBON WHISKEY</p>

    <p class="badge-text left">SINGLE<br>BARREL</p>
    <div class="brand-mark">
      <div class="ring"></div>
      <div class="name">NIGHTFALL</div>
    </div>
    <p class="badge-text right">CASK<br>STRENGTH</p>

    <div class="age-mark">
      <span class="rule" style="top:16px"></span>
      <span class="rule" style="top:68px"></span>
      <span class="word" style="left:0">AGED</span>
      <span class="num">17</span>
      <span class="word" style="left:105px">YEARS</span>
    </div>

    <span class="field-label" style="left:18px">ALC/VOL</span>
    <div class="field-box" style="left:29px"></div>
    <span class="field-label" style="left:405px">BARREL NO</span>
    <div class="field-box" style="left:411px"></div>
  </section>

  <section class="back-label">
    <div class="back-photo" role="img" aria-label="Faded photo of the racing horse and jockey"></div>
    <div class="company-mark">
      <div class="ring"></div>
      <div class="name">NIGHTFALL<br>BARREL</div>
      <div class="sub">— COMPANY —</div>
    </div>
    <h2 class="edition">Winners Series<br>Rolling Verdict Edition<br>Single Barrel No.45</h2>
    <p class="story one">The Nightfall Racing Winners Series honors the horses who have brought home victories for our stable. This edition celebrates Rolling Verdict and her maiden victory on May 28, 2021.</p>
    <p class="story two">Raise a glass to her incredible career with this non-chill filtered single barrel crafted in her honor. Here’s to Rolling Verdict a true champion!</p>
    <p class="maker">Bottled by Old Riverbend Whiskey Co., Louisville, Kentucky<br>Distilled in Bardstown. Kentucky</p>
    <p class="site">NIGHTFALL-GROUP.COM</p>
    <p class="warning">GOVERNMENT WARNING: (1) According to the Surgeon General, women should not drink alcoholic beverages during pregnancy because of the risk of birth defects. (2) Consumption of alcoholic beverages impairs your ability to drive a car or operate machinery, and may cause health problems.</p>
    <p class="volume">750ML</p>
  </section>
</main>
</body>
</html>
```